Marlow Ridge Dental business card

Business card would have following info:

Alden R. Kasprzak, DMD, FAGD
General Dentist
email: office@marlowridgedental.example
phone: 617-490-3867
fax: 617-490-3867
website: marlowridgedental.example

second side would have lines for:

appointment date
appointment time

```html
<!DOCTYPE html>
<html lang="en">
<head>
<meta charset="utf-8">
<title>Marlow Ridge Dental – Business Card</title>
<link rel="stylesheet" href="https://fonts.googleapis.com/css2?family=Montserrat:wght@500;600;700&family=Raleway:ital,wght@0,500;1,500&family=Poppins:wght@500&display=swap">
<style>
  :root {
    --brand-blue: #1e7bbf;
    --white: #ffffff;
    --faint-blue: #c9dff0;
    --backdrop: #2e2e2e;
  }
  * { margin: 0; padding: 0; box-sizing: border-box; }
  html, body { width: 1200px; height: 1200px; overflow: hidden; }
  body { background: var(--backdrop); position: relative; font-family: "Montserrat", sans-serif; }

  .card {
    position: absolute;
    left: 119px;
    width: 962px;
    height: 564px;
    border-radius: 22px;
    overflow: hidden;
  }
  .card-front { top: 20px; background: var(--brand-blue); color: var(--white); }
  .card-back { top: 618px; background: var(--white); color: var(--brand-blue); font-family: "Raleway", sans-serif; }

  /* front */
  .wordmark {
    position: absolute; left: 65px; top: 128px; width: 410px;
    font-family: "Montserrat", sans-serif; font-weight: 500; text-transform: uppercase;
    color: var(--white);
  }
  .wordmark-main { font-size: 35px; letter-spacing: 3px; line-height: 1.1; white-space: nowrap; }
  .wordmark-sub { display: flex; align-items: center; gap: 16px; font-size: 26px; letter-spacing: 14px; margin-top: 4px; }
  .wordmark-sub .rule { flex: 1; height: 2px; background: var(--white); }
  .wordmark-sub span.word { margin-right: -14px; }

  .dentist-name { position: absolute; left: 65px; top: 272px; font-size: 37px; font-weight: 700; white-space: nowrap; }
  .credentials { position: absolute; left: 365px; top: 321px; width: 100px; text-align: right; font-size: 16px; font-weight: 600; }
  .role { position: absolute; left: 69px; top: 330px; font-size: 27px; font-weight: 500; }

  .contact-list { position: absolute; left: 61px; top: 393px; list-style: none; }
  .contact-list li { display: flex; align-items: center; gap: 14px; height: 31px; font-size: 24px; font-weight: 600; white-space: nowrap; }
  .contact-list svg { width: 30px; height: 24px; flex: none; }

  .mark-circle { position: absolute; left: 562px; top: 104px; width: 384px; height: 384px; border: 5px solid var(--white); border-radius: 50%; }

  /* back */
  .faint-circle { position: absolute; left: 540px; top: 84px; width: 440px; height: 440px; border: 6px solid var(--faint-blue); border-radius: 50%; }

  .field { position: absolute; font-size: 26px; font-weight: 500; white-space: nowrap; }
  .fill-line { position: absolute; height: 2px; background: var(--brand-blue); }

  .appointment-note { position: absolute; left: 0; width: 942px; top: 130px; text-align: center; font-style: italic; font-size: 26px; font-weight: 500; }

  .day-row { position: absolute; left: 110px; top: 226px; display: flex; gap: 26px; font-size: 27px; font-weight: 500; }
  .day { display: flex; align-items: center; gap: 4px; }
  .day .box { width: 15px; height: 15px; border: 2px solid var(--brand-blue); }

  .footnote { position: absolute; left: 58px; top: 448px; font-family: "Poppins", sans-serif; font-size: 15.5px; font-weight: 500; line-height: 23px; }
</style>
</head>
<body>

<section class="card card-front" aria-label="Card front">
  <div class="wordmark">
    <div class="wordmark-main">Marlow Ridge</div>
    <div class="wordmark-sub"><span class="rule"></span><span class="word">Dental</span><span class="rule"></span></div>
  </div>

  <h1 class="dentist-name">Alden R. Kasprzak</h1>
  <p class="credentials">DMD, FAGD</p>
  <p class="role">General Dentist</p>

  <ul class="contact-list">
    <li>
      <svg viewBox="0 0 30 24" aria-hidden="true"><rect x="1" y="3" width="28" height="18" fill="#fff"/><path d="M1 3 L15 14 L29 3 M1 21 L11 11 M29 21 L19 11" stroke="#1e7bbf" stroke-width="2" fill="none"/></svg>
      office@marlowridgedental.example
    </li>
    <li>
      <svg viewBox="0 0 30 24" aria-hidden="true"><path d="M8 2 C5 3 3 6 5 11 C8 17 13 21 18 22 C22 23 24 20 24 18 L19 14 L16 16 C13 15 10 11 9 8 L11 5 Z" fill="#fff"/></svg>
      617-490-3867
    </li>
    <li>
      <svg viewBox="0 0 30 24" aria-hidden="true"><circle cx="14" cy="12" r="10" fill="none" stroke="#fff" stroke-width="2"/><path d="M4 12 H24 M14 2 V22 M14 2 C9 7 9 17 14 22 M14 2 C19 7 19 17 14 22" stroke="#fff" stroke-width="1.6" fill="none"/></svg>
      www.marlowridgedental.example
    </li>
  </ul>

  <div class="mark-circle" aria-hidden="true"></div>
</section>

<section class="card card-back" aria-label="Card back, appointment reminder">
  <div class="faint-circle" aria-hidden="true"></div>

  <span class="field" style="left:56px; top:91px;">Name :</span>
  <span class="fill-line" style="left:156px; top:115px; width:730px;"></span>

  <p class="appointment-note">Has an appointment on</p>

  <div class="day-row">
    <span class="day"><span class="box"></span>Mon.</span>
    <span class="day"><span class="box"></span>Tues.</span>
    <span class="day"><span class="box"></span>Wed.</span>
    <span class="day"><span class="box"></span>Thurs.</span>
    <span class="day"><span class="box"></span>Fri.</span>
    <span class="day"><span class="box"></span>Sat.</span>
    <span class="day"><span class="box"></span>Sun.</span>
  </div>

  <span class="field" style="left:57px; top:302px;">Date :</span>
  <span class="fill-line" style="left:143px; top:328px; width:336px;"></span>
  <span class="field" style="left:498px; top:302px;">Time :</span>
  <span class="fill-line" style="left:588px; top:328px; width:147px;"></span>
  <span class="field" style="left:747px; top:302px;">A.M. / P.M.</span>

  <span class="field" style="left:56px; top:356px;">Details :</span>
  <span class="fill-line" style="left:170px; top:382px; width:716px;"></span>
  <span class="fill-line" style="left:58px; top:425px; width:828px;"></span>

  <p class="footnote">If you are unable to keep your appointment.<br>Please contact us as soon as possible.</p>
</section>

</body>
</html>
```